Charity auction mobile bidding site

Our charities can build their own event landing page to promote their silent auction fundraising event. We need a top menu, hero image with event title and desc, a register/login area, up to 4 content blocks and an auction listing of items in a grid dynamically created from their catalog. Currently we have this laid out in 100% width layers or stacks. It needs to be mobile friendly first. Examples include kvtrial.plq.example and lindvar.plq.example and gabscheck.plq.example We need to allow people to design nice sites instead of PalNook pages that look terrible.

Target Market(s)

Soccer moms and volunteers who feel like rockstars when they learn how to use chumwall or clipboardly. Not super savvy so less is more. Not overwhelming. Clean with whitespace and functional is what they want

Number of Pages Required

1 page

Font styles to use
Sans Serif

Colors

Designer to choose colors to be used in the design.

Requirements
Must have
• Nothing so tightly designed that it would look terrible if an organization loaded their own photos. This means the hero image could be landscape or portrait. When in doubt, keep it clean and simple. A one or two color palette
Nice to have
• A pop up concept for someone to log in when they choose to bid on an item in the preview.
Should not have
• Decorative fonts. Too many colors.

```html
<!DOCTYPE html>
<html lang="en">
<head>
<meta charset="utf-8">
<title>Auction Item – Place a Bid</title>
<link href="https://fonts.googleapis.com/css2?family=Lato:wght@400;700;900&display=swap" rel="stylesheet">
<style>
  :root {
    --brand-blue: #1f4a9e;
    --brand-blue-soft: #9badd3;
    --ink: #333333;
    --ink-muted: #4a4a4a;
    --line: #dcdcdc;
    --paper: #ffffff;
    --photo-warm: #ee9450;
  }
  * { box-sizing: border-box; margin: 0; padding: 0; }
  html, body {
    width: 1200px; height: 675px; overflow: hidden;
    background: var(--paper);
    font-family: "Lato", Arial, sans-serif;
    color: var(--ink);
  }
  .stage { position: relative; width: 1200px; height: 675px; overflow: hidden; }

  /* Page behind the popup */
  .page-backdrop {
    position: absolute; inset: 0;
    filter: blur(2.5px);
    opacity: 0.7;
  }
  .story-heading {
    position: absolute; left: 350px; top: 60px; width: 500px;
    text-align: center; font-weight: 900; font-size: 22px; line-height: 33px;
    color: #6f8cc9;
  }
  .auction-card { position: absolute; top: 235px; width: 164px; }
  .auction-card .card-photo { height: 227px; background: linear-gradient(160deg, #8fa0a8, #6f7d74 55%, #b7b0a3); }
  .auction-card .card-price {
    position: absolute; top: 290px; width: 100%; text-align: center;
    font-size: 17px; font-weight: 700; color: #7a7a7a;
  }
  .auction-card .card-bid {
    position: absolute; top: 320px; left: 29px; width: 106px; height: 31px;
    background: #6f8cc9; color: #fff; font-size: 8px; font-weight: 700;
    display: flex; align-items: center; justify-content: center;
  }
  .footer-band { position: absolute; left: 0; right: 0; top: 648px; height: 27px; background: var(--brand-blue-soft); }

  /* Bid popup */
  .bid-modal {
    position: absolute; left: 274px; top: 119px; width: 644px; height: 409px;
    background: var(--paper); display: flex;
    box-shadow: 0 0 0 1px #e4e4e4;
  }
  .item-photo {
    width: 269px; height: 100%;
    background: linear-gradient(180deg, #ea8447 0%, var(--photo-warm) 55%, #d68a48 100%);
  }
  .bid-panel { position: relative; flex: 1; }
  .close-icon { position: absolute; left: 344px; top: 20px; }
  .item-title {
    position: absolute; top: 41px; left: 0; width: 100%;
    text-align: center; font-weight: 700; font-size: 27px; line-height: 31px; color: var(--ink);
  }
  .item-description {
    position: absolute; top: 121px; left: 42px; width: 272px;
    text-align: center; font-size: 10px; line-height: 18.2px; color: var(--ink-muted);
  }
  .bid-stat { position: absolute; top: 209px; width: 150px; text-align: center; }
  .bid-stat.started { left: 30px; }
  .bid-stat.current { left: 183px; }
  .bid-stat .stat-label { font-size: 11.3px; color: var(--ink-muted); }
  .bid-stat .stat-value { font-size: 20px; font-weight: 700; color: #555; margin-top: 4px; }
  .bid-stat.current .stat-value { color: var(--brand-blue); }
  .your-bid-label {
    position: absolute; top: 271px; left: 0; width: 100%;
    text-align: center; font-size: 11.3px; color: var(--ink-muted);
  }
  .bid-input {
    position: absolute; left: 105px; top: 290px; width: 145px; height: 48px;
    border: 1px solid var(--line); display: flex;
  }
  .bid-amount {
    flex: 1; display: flex; align-items: center; justify-content: center;
    font-size: 22px; font-weight: 700; color: var(--ink);
  }
  .bid-steppers { width: 24px; display: flex; flex-direction: column; border-left: 1px solid var(--line); }
  .step-up { height: 24px; background: var(--brand-blue); display: flex; align-items: center; justify-content: center; }
  .step-down { flex: 1; display: flex; align-items: center; justify-content: center; }
  .bid-now {
    position: absolute; left: 0; right: 0; bottom: 0; height: 41px;
    background: var(--brand-blue); color: #fff;
    font-size: 11.5px; font-weight: 700; letter-spacing: 0.2px;
    display: flex; align-items: center; justify-content: center;
  }
</style>
</head>
<body>
<div class="stage">
  <div class="page-backdrop" aria-hidden="true">
    <h2 class="story-heading">A Partnership for the Long Haul: Kindbridge and Hallway Home Collaborate for Long-Term</h2>
    <div class="auction-card" style="left:234px"><div class="card-photo"></div><div class="card-price">$10</div><div class="card-bid">BID</div></div>
    <div class="auction-card" style="left:424px"><div class="card-photo"></div><div class="card-price">$2,500</div><div class="card-bid">BID</div></div>
    <div class="auction-card" style="left:612px"><div class="card-photo"></div><div class="card-price">$250</div><div class="card-bid">BID</div></div>
    <div class="auction-card" style="left:799px"><div class="card-photo" style="background:linear-gradient(160deg,#c9c2b4,#8a7a62 60%,#5b4a3a)"></div><div class="card-price">$80</div><div class="card-bid">BID</div></div>
    <div class="footer-band"></div>
  </div>

  <div class="bid-modal" role="dialog" aria-label="Place a bid">
    <div class="item-photo" role="img" aria-label="Photo of the auction item: a cruise ship at sea at sunset"></div>
    <div class="bid-panel">
      <svg class="close-icon" width="11" height="11" viewBox="0 0 11 11" aria-label="Close">
        <path d="M1 1 L10 10 M10 1 L1 10" stroke="#9a9a9a" stroke-width="1.2"/>
      </svg>
      <h1 class="item-title">A Cruise around the<br>world</h1>
      <p class="item-description">We’ll be there in the early days with personal care items, supplies for shelters, and cleaning/mucking out products and we’ll be there long after the media spotlight has dimmed months and year.</p>
      <div class="bid-stat started">
        <div class="stat-label">Started&nbsp; at</div>
        <div class="stat-value">$2,500</div>
      </div>
      <div class="bid-stat current">
        <div class="stat-label">Current bid&nbsp; at</div>
        <div class="stat-value">$3,240</div>
      </div>
      <div class="your-bid-label">Your bid</div>
      <div class="bid-input">
        <div class="bid-amount">$3,500</div>
        <div class="bid-steppers">
          <div class="step-up"><svg width="11" height="7" viewBox="0 0 11 7"><path d="M1 6 L5.5 1.5 L10 6" fill="none" stroke="#fff" stroke-width="1.4"/></svg></div>
          <div class="step-down"><svg width="11" height="7" viewBox="0 0 11 7"><path d="M1 1 L5.5 5.5 L10 1" fill="none" stroke="#c4c4c4" stroke-width="1.2"/></svg></div>
        </div>
      </div>
      <div class="bid-now">BID NOW</div>
    </div>
  </div>
</div>
</body>
</html>
```